Flyer-Design für Karin Dossow
Zielgruppe
Ich bin psychologische Beraterin und Heilpraktikerin für Psychotherapie. Ich biete ein Coaching speziell für Mütter (meist Mütter mit neugeborenen Babys) an. Dieses Mütter-Coaching will ich bewerben. Die Flyer werden unter anderen an Ärzte und Hebammen weiter gegeben und dort in den Praxen ausliegen.
Aufgabenstellung
In meinem Logo herrschen die Farben orange und grau vor - es wäre schön, wenn sich diese Farben im Flyer wiederfinden würden - evtl. kombiniert mit mittelblau oder einem hellem grün.
Des weiteren möchte ich später Flyer im Din Lang Format (einseitig) mit anderen Angeboten erstellen. Das sollte mit dem Design dann auch möglich sein.
Der Schrifttyp soll bitte Arial sein, passend zum Logo. Ich habe bei Bildarko Fotos zu dem Thema erstanden, die ich stimmig finde. Diese Bilder sollten im Flyer genutzt werden.
Für diesen Flyer hätte ich gerne das Format: Falzblatt mit Wickelfalz - 279 x 219 mm

```html
<!DOCTYPE html>
<html lang="de">
<head>
<meta charset="utf-8">
<title>Falzblatt – Coaching für Mütter</title>
<link href="https://fonts.googleapis.com/css2?family=Arimo:wght@400;700&display=swap" rel="stylesheet">
<style>
:root{
  --orange:#e9a13b;
  --orange-dark:#d98e26;
  --grey:#6e6e6e;
  --grey-dark:#5c5c5c;
  --grey-text:#555;
  --paper:#efefef;
  --paper-shade:#dcdcdc;
  --white:#ffffff;
  --stage:#4b4b4b;
}
*{box-sizing:border-box;margin:0;padding:0}
html,body{width:1200px;height:600px;overflow:hidden}
body{background:var(--stage);font-family:"Arimo",Arial,sans-serif;color:var(--grey-text);position:relative}
.sheet{position:absolute;top:75px;width:570px;height:450px;display:flex;box-shadow:0 6px 18px rgba(0,0,0,.35)}
.sheet--inside{left:20px}
.sheet--outside{left:610px}
.panel{width:190px;height:100%;position:relative;overflow:hidden;display:flex;flex-direction:column}
.photo{background:linear-gradient(160deg,#cfd3d8,#a9adb3 55%,#8d8680);}

/* inside – panel 1 */
.situation__photo{height:150px;position:relative}
.situation__title{position:absolute;left:0;right:0;bottom:0;padding:6px 12px;background:rgba(255,255,255,.55);font-weight:700;font-size:22px;line-height:1;color:#333;letter-spacing:-.5px}
.situation__list{flex:1;background:var(--orange);list-style:none;padding:12px 12px 0 14px;color:var(--white);font-size:7px;line-height:1.35}
.situation__list li{margin-bottom:9px;padding-left:7px;position:relative}
.situation__list li::before{content:"•";position:absolute;left:0}

/* inside – panel 2 */
.support{background:linear-gradient(90deg,var(--paper-shade),var(--paper) 20%,var(--white));padding:22px 14px 0 14px}
.support__title{font-weight:700;font-size:15px;line-height:1.05;color:#333;margin-bottom:14px}
.support__head{color:var(--orange);font-weight:700;font-size:11px;margin:10px 0 4px}
.support p{font-size:6.8px;line-height:1.4;margin-bottom:5px}
.support__note{margin-top:auto;margin-bottom:16px;background:var(--orange);color:var(--white);border-radius:14px;padding:7px 12px;font-size:5.6px;line-height:1.35;text-align:center}

/* inside – panel 3 */
.way{background:var(--grey)}
.way__intro{padding:18px 12px 8px;color:var(--white)}
.way__title{font-weight:700;font-size:19px;line-height:1}
.way__sub{font-size:6px;font-weight:700;text-transform:uppercase;margin-top:4px;color:#e6e6e6}
.way__steps{flex:1;display:flex;flex-direction:column}
.step{flex:1;display:flex;align-items:center;gap:8px;padding:0 10px;font-size:7px;line-height:1.35;color:var(--white)}
.step:nth-child(odd){background:var(--orange)}
.step:nth-child(even){background:var(--grey-dark)}
.step svg{flex:none;width:24px;height:24px}

/* outside – panel 1 */
.why{background:var(--grey)}
.why__head{background:var(--grey-dark);padding:18px 12px 12px;color:var(--white)}
.why__title{font-weight:700;font-size:12px;line-height:1.15}
.why__claim{font-size:6px;font-weight:700;margin-top:5px}
.why__band{background:var(--orange);padding:12px 14px;color:var(--white);font-weight:700;font-size:16px;line-height:1.05;height:68px}
.why__body{padding:12px 14px;color:#ececec;font-size:6.4px;line-height:1.45;flex:1;position:relative}
.why__body p{margin-bottom:8px}
.why__start{width:80px}
.why__badge{position:absolute;right:10px;bottom:18px;width:90px;height:90px;border-radius:50%;background:var(--orange);color:var(--white);font-weight:700;font-size:9px;line-height:1.3;display:flex;align-items:center;justify-content:center;text-align:center;padding:10px;box-shadow:0 2px 6px rgba(0,0,0,.25)}

/* logo block */
.brand{padding:18px 14px 10px}
.brand__name{display:flex;align-items:center;gap:4px;font-weight:700;font-size:14px;color:var(--grey)}
.brand__dot{width:8px;height:8px;border-radius:50%;background:var(--orange)}
.brand__tag{color:var(--orange);font-weight:700;font-size:8px;margin-top:7px}
.brand__sub{font-size:5px;font-weight:700;color:#444;margin-top:1px}

/* outside – panel 2 */
.offers{background:linear-gradient(90deg,var(--paper-shade),var(--paper) 15%,var(--white))}
.offer{display:flex;gap:8px;padding:9px 10px;height:64px;color:var(--white)}
.offer--orange{background:var(--orange)}
.offer--grey{background:var(--grey)}
.offer svg{flex:none;width:26px;height:26px}
.offer__title{font-weight:700;font-size:8.5px;margin-bottom:3px}
.offer__text{font-size:5.8px;line-height:1.35}
.contact{padding:12px 14px;font-size:6px;line-height:1.45;color:#444}
.contact__call{color:var(--orange);font-weight:700;margin-bottom:6px}
.contact__name{color:var(--orange);font-weight:700}
.contact__role{font-weight:700;margin-bottom:5px}
.contact__phone{color:var(--orange);font-weight:700;margin-bottom:5px}
.contact__mail{margin-bottom:5px}

/* outside – panel 3 */
.cover{background:linear-gradient(90deg,var(--paper-shade),var(--white) 20%)}
.cover__photo{height:185px}
.cover__claim{flex:1;background:var(--orange);color:var(--white);font-size:17px;line-height:1.3;padding:16px 16px}
.cover__claim strong{font-weight:700}
</style>
</head>
<body>

<section class="sheet sheet--inside">
  <article class="panel situation">
    <div class="situation__photo photo" role="img" aria-label="Foto: erschöpfte Mutter mit schlafendem Baby">
      <h2 class="situation__title">IHRE<br>SITUATION</h2>
    </div>
    <ul class="situation__list">
      <li>Haben Sie sich Ihr Mutterglück anders vorgestellt? - Sie hatten sich so auf Ihr Baby gefreut, aber die Realität ist gar nicht so, wie Sie sich das gedacht haben?</li>
      <li>Oder Sie haben bereits ein oder mehrere Kinder aber trotzdem ist jetzt alles anders?</li>
      <li>Fühlen Sie sich allein, isoliert: Ihre Kollegen und Freunde führen weiterhin Ihr früheres Leben - Sie sind aber nicht mehr mit dabei?</li>
      <li>Das Verständnis Ihrer Umgebung für Ihre neue Situation fehlt. Sogar die Partnerschaft ist plötzlich ganz anders als sie es vorher war?</li>
      <li>Sie werden nur noch als Mutter wahrgenommen - kaum mehr als die Frau und die Persönlichkeit, die Sie vorher waren und auch immer noch sind?</li>
      <li>Sie fühlen sich oft erschöpft, ratlos, überfordert, unverstanden?</li>
    </ul>
  </article>

  <article class="panel support">
    <h2 class="support__title">MEINE<br>UNTERSTÜTZUNG</h2>
    <h3 class="support__head">BEGLEITUNG</h3>
    <p>Die gute Nachricht: Sie müssen diese belastende Situation nicht allein bewältigen - erleben Sie Erleichterung, indem Sie sich von mir beraten lassen.</p>
    <p>Als Coach gehe ich ganz individuell auf Ihre Person und auf Ihre persönliche Situation ein.</p>
    <h3 class="support__head">STÄRKUNG</h3>
    <p>Entscheiden Sie sich für einen Weg, der zu Ihnen passt und Sie glücklich macht.</p>
    <p>Finden Sie die Mutterrolle, die es Ihnen ermöglicht, gut für sich zu sorgen und bei sich zu bleiben. Leben Sie so Ihre Bedürfnisse und Interessen im Einklang mit denen Ihrer Familie.</p>
    <h3 class="support__head">BERATUNG</h3>
    <p>Trotz einer Flut an Informationen fühlen sich viele Mütter mit ihren Themen alleine gelassen, hilflos und überfordert.</p>
    <p>Bei mir bleiben Sie nicht allein und ratlos: zusammen finden wir individuelle Antworten auf Ihre ganz persönlichen Fragen.</p>
    <p class="support__note">Hinweis: Es handelt sich hier um eine Beratung und nicht um eine Psychotherapie oder sonstige Heilkunde im gesetzlichen Sinne und soll diese auch nicht ersetzen.</p>
  </article>

  <article class="panel way">
    <header class="way__intro">
      <h2 class="way__title">UNSER WEG</h2>
      <p class="way__sub">Gemeinsam können wir uns Ihre Themen ansehen und bearbeiten</p>
    </header>
    <div class="way__steps">
      <div class="step"><svg viewBox="0 0 24 24"><circle cx="12" cy="12" r="12" fill="#fff" fill-opacity=".3"/><circle cx="12" cy="8" r="2.5" fill="#fff"/><path d="M6 17h12l-3-5H9z" fill="#fff"/></svg><span>Stressbewältigung - finden Sie den Weg zu mehr Gelassenheit, zur inneren Ruhe</span></div>
      <div class="step"><svg viewBox="0 0 24 24"><circle cx="12" cy="12" r="12" fill="#e9a13b"/><circle cx="12" cy="12" r="6" fill="none" stroke="#fff" stroke-width="1.5"/><path d="M12 8v4h3" stroke="#fff" stroke-width="1.5" fill="none"/></svg><span>Zeiteinteilung - so passen Sie Ihre Zeit der momentanen Situation an</span></div>
      <div class="step"><svg viewBox="0 0 24 24"><circle cx="12" cy="12" r="12" fill="#fff" fill-opacity=".3"/><rect x="11" y="6" width="2" height="8" fill="#fff"/><circle cx="12" cy="17" r="1.3" fill="#fff"/></svg><span>Erhalten Sie mehr Klarheit über Ihre Bedürfnisse und Erwartungen</span></div>
      <div class="step"><svg viewBox="0 0 24 24"><circle cx="12" cy="12" r="12" fill="#e9a13b"/><path d="M8 6v12M12 6v12M16 6v12" stroke="#fff" stroke-width="1.3"/><rect x="6.5" y="9" width="3" height="2" fill="#fff"/><rect x="10.5" y="13" width="3" height="2" fill="#fff"/><rect x="14.5" y="8" width="3" height="2" fill="#fff"/></svg><span>Wandeln Sie Unsicherheit in Stabilität um</span></div>
      <div class="step"><svg viewBox="0 0 24 24"><circle cx="12" cy="12" r="12" fill="#fff" fill-opacity=".3"/><circle cx="12" cy="11" r="5" fill="#fff"/><rect x="10" y="15" width="4" height="3" fill="#fff"/></svg><span>Erkennen und nutzen Sie Ihre Stärken und Fähigkeiten</span></div>
      <div class="step"><svg viewBox="0 0 24 24"><circle cx="12" cy="12" r="12" fill="#e9a13b"/><circle cx="9" cy="8" r="2" fill="#fff"/><circle cx="15" cy="9" r="1.6" fill="#fff"/><path d="M6 18v-5a3 3 0 0 1 6 0v5zM13 18v-4a2 2 0 0 1 4 0v4z" fill="#fff"/></svg><span>Familienberatung - so können Sie entgegenkommend miteinander umgehen</span></div>
      <div class="step"><svg viewBox="0 0 24 24"><circle cx="12" cy="12" r="12" fill="#fff" fill-opacity=".3"/><path d="M12 12L7 7M12 12l6-3M12 12l-4 6M12 12l5 5" stroke="#fff" stroke-width="1"/><circle cx="12" cy="12" r="2" fill="#fff"/><circle cx="7" cy="7" r="1.4" fill="#fff"/><circle cx="18" cy="9" r="1.4" fill="#fff"/><circle cx="8" cy="18" r="1.4" fill="#fff"/><circle cx="17" cy="17" r="1.4" fill="#fff"/></svg><span>Netzwerk - hier finden Sie Verständnis und Unterstützung</span></div>
    </div>
  </article>
</section>

<section class="sheet sheet--outside">
  <article class="panel why">
    <header class="why__head">
      <h2 class="why__title">WARUM COACHING<br>EXTRA FÜR MÜTTER?</h2>
      <p class="why__claim">Nur! Nur wer gut für sich selbst sorgt, kann auch für andere da sein!</p>
    </header>
    <h2 class="why__band">COACHING<br>FÜR MÜTTER</h2>
    <div class="why__body">
      <p>Als Heilpraktikerin für Psychotherapie und geprüfte psychologische Beraterin habe ich mich besonders auf das Coaching für Mütter spezialisiert.</p>
      <p>Ich setzte dabei die Methode des lösungsorientierten Kurzzeitcoachings ein, das den Fokus auf Stärken und Lösungen legt und nicht die Probleme und Hindernisse in den Vordergrund stellt.</p>
      <p>Das Konzept wird durch Achtsamkeits- und Entspannungsübungen abgerundet. Aspekte der „gewaltfreien" = wertschätzenden Kommunikation werden für individuelle Konfliktlösungen im familiären Alltag genutzt.</p>
      <p class="why__start">Starten Sie mit einem neuen und liebevollen Blick auf Ihr Leben und auf Ihre Fähigkeiten.</p>
      <p class="why__badge">Sie werden erstaunt sein, was alles in Ihnen wohnt.</p>
    </div>
  </article>

  <article class="panel offers">
    <header class="brand">
      <p class="brand__name">karindossow<span class="brand__dot"></span></p>
      <p class="brand__tag">COACHING FÜR MÜTTER</p>
      <p class="brand__sub">BEGLEITUNG - STÄRKUNG - BERATUNG</p>
    </header>
    <div class="offer offer--orange">
      <svg viewBox="0 0 26 26"><circle cx="13" cy="13" r="13" fill="#fff" fill-opacity=".35"/><circle cx="13" cy="10" r="3.5" fill="#fff"/><path d="M6 21a7 7 0 0 1 14 0z" fill="#fff"/></svg>
      <div><h3 class="offer__title">EINZELCOACHING</h3><p class="offer__text">Sie können wählen: das Coaching kann in meiner Praxis in Ahrenfeld oder gern auch bei Ihnen zu Hause stattfinden, allein oder mit Partner, so wie es gerade für Sie am besten passt.</p></div>
    </div>
    <div class="offer offer--grey">
      <svg viewBox="0 0 26 26"><circle cx="13" cy="13" r="13" fill="#e9a13b"/><circle cx="13" cy="9" r="2.5" fill="#fff"/><circle cx="8" cy="12" r="2" fill="#fff"/><circle cx="18" cy="12" r="2" fill="#fff"/><path d="M8 20a5 5 0 0 1 10 0z" fill="#fff"/></svg>
      <div><h3 class="offer__title">GRUPPENCOACHING</h3><p class="offer__text">Lernen Sie Gleichgesinnte kennen und profitieren Sie in doppelter Hinsicht - nach dem Motto: „Lieber gemeinsam als einsam".</p></div>
    </div>
    <div class="offer offer--orange">
      <svg viewBox="0 0 26 26"><circle cx="13" cy="13" r="13" fill="#fff" fill-opacity=".35"/><rect x="9" y="6" width="8" height="14" rx="1.5" fill="none" stroke="#fff" stroke-width="1.5"/><circle cx="13" cy="17.5" r=".9" fill="#fff"/></svg>
      <div><h3 class="offer__title">TELEFONCOACHING</h3><p class="offer__text">Sie bestimmen Ort und Zeit. Dieses Angebot könnte das Richtige für Sie sein, wenn Sie zeitlich oder örtlich gebunden sind.</p></div>
    </div>
    <address class="contact" style="font-style:normal">
      <p class="contact__call">Rufen Sie mich doch einfach unverbindlich an.<br>Ich freue mich auf Sie!</p>
      <p class="contact__name">Karin Dossow</p>
      <p class="contact__role">Heilpraktikerin für Psychotherapie<br>Geprüfte Psychologische Beraterin</p>
      <p class="contact__phone">Telefon: 0170 - 4418 2206</p>
      <p class="contact__mail">Email: info@karin-dossow.de<br>www.karin-dossow.de</p>
      <p>Praxisgemeinschaft am Lindenhof<br>Fliederweg 14<br>40721 Ahrenfeld</p>
    </address>
  </article>

  <article class="panel cover">
    <header class="brand">
      <p class="brand__name">karindossow<span class="brand__dot"></span></p>
      <p class="brand__tag">COACHING FÜR MÜTTER</p>
      <p class="brand__sub">BEGLEITUNG - STÄRKUNG - BERATUNG</p>
    </header>
    <div class="cover__photo photo" role="img" aria-label="Foto: Mutter hält ihr schlafendes Neugeborenes an der Schulter"></div>
    <h1 class="cover__claim" style="font-weight:400">DAS BABY IST DA<br>UND <strong>NICHTS</strong><br>IST MEHR<br>WIE ES WAR!</h1>
  </article>
</section>

</body>
</html>
```